VOLT - Monitoring Natural Hazards from Space Web Application

KORMEL Sarl is a Luxembourg based Space-Startup that works in the field of Earth Observation. KORMEL is a platform able to extract value-added information from satellite data and is specialized in mapping Natural Disaster (floods, fires etc).

We are now developing a new vertical tool, called VOLT, dedicated to the monitoring of natural hazards in Humanitarian Camps around the world.

The goal of VOLT is to hide to the users' all the complexity of the Satellite Image processing and just provide them the results.

This project require to Design 4 pages of VOLT:
• Public Home Page (Code - V01)
• Dashboard (private Home Page) (Code - V03)
• Monitor (web GIS) (Code - V14)
• Registration Page (Code - V04)

We would like to provide the required time to make a good job.

Target Market(s)

Humanitarian Agencies, Goverments

Coding

Coded - Design and coding required

Number of Pages Required

4 page

Font styles to use
Other font styles liked:
• see the manual attached

Requirements
Must have
• 4 pages. One Home, one form, one dashboard and one web map.
Nice to have
• Please read the attachment with all the detailed instructions

```html
<!DOCTYPE html>
<html lang="en">
<head>
<meta charset="utf-8">
<title>VOLT – Monitoring Natural Hazards from Space</title>
<link href="https://fonts.googleapis.com/css2?family=Barlow+Condensed:wght@400;500&family=Montserrat:wght@400;500;600;700&display=swap" rel="stylesheet">
<style>
:root{
  --navy:#062c43;
  --navy-soft:#0d3a53;
  --gold:#f0b323;
  --ink:#0b2e44;
  --text:#33414b;
  --muted:#7d8a93;
  --mist:#dfe5e8;
  --paper:#f8f8f8;
  --white:#ffffff;
}
*{box-sizing:border-box;margin:0;padding:0}
html,body{width:1200px;height:3497px;overflow:hidden}
body{position:relative;background:var(--white);font-family:"Montserrat",sans-serif;color:var(--text)}
.abs{position:absolute}
.display{font-family:"Barlow Condensed",sans-serif;font-weight:400;letter-spacing:2px;text-transform:uppercase;color:var(--ink)}
.eyebrow{font-size:10px;font-weight:700;color:var(--ink);text-transform:uppercase;display:flex;align-items:center;gap:10px}
.eyebrow::after{content:"";display:block;height:1px;background:#b9c3c9}
.btn-outline{display:flex;align-items:center;justify-content:center;border:1.5px solid var(--ink);border-radius:20px;font-size:10px;font-weight:700;color:var(--ink);text-transform:uppercase;letter-spacing:.5px}

/* hero */
.hero{left:0;top:0;width:1200px;height:640px;background:radial-gradient(ellipse at 62% 55%,#3a2a12 0%,#1a140b 30%,#050505 65%)}
.hero-arcs{left:0;top:0;width:1200px;height:800px}
.brand{left:95px;top:38px;display:flex;align-items:center;gap:12px}
.brand-dot{width:40px;height:40px;border:2px solid var(--gold);border-radius:50%}
.brand-name{font-family:"Montserrat",sans-serif;font-weight:500;font-size:30px;letter-spacing:4px;color:var(--white)}
.nav{top:54px;left:786px;display:flex;gap:25px;font-size:10px;font-weight:700;color:var(--white)}
.nav .active{color:var(--gold)}
.hero-title{left:0;top:232px;width:1200px;text-align:center;font-size:41px;line-height:45px;color:var(--white);letter-spacing:3px}
.hero-btn{left:535px;top:348px;width:130px;height:30px;border-color:var(--white);color:var(--white);font-size:9px}

/* features */
.mark-ring{left:95px;top:670px;width:410px;height:410px;border:14px solid var(--mist);border-radius:50%}
.features-label{left:99px;top:740px}
.features-label::after{width:104px}
.features-title{left:97px;top:766px;width:420px;font-size:27px;line-height:30px}
.card{width:251px;height:175px;background:var(--white);border-radius:10px;box-shadow:0 6px 24px rgba(6,44,67,.08);padding:24px 24px 0 26px}
.card-head{display:flex;align-items:center;gap:14px;height:52px}
.card-head svg{width:52px;height:52px;flex:none}
.card-title{font-size:12px;font-weight:700;color:var(--ink)}
.card-text{margin-top:20px;font-size:11px;line-height:15px;color:var(--text)}

/* mission */
.mission{left:0;top:1219px;width:1200px;height:502px;background:var(--paper)}
.photo-night{left:95px;top:1301px;width:190px;height:253px;background:linear-gradient(160deg,#0d1522 0%,#3b2a1c 45%,#6a4524 70%,#0f1a26 100%)}
.photo-frame{left:300px;top:1203px;width:297px;height:420px;background:var(--mist)}
.photo-couple{left:265px;top:1187px;width:316px;height:458px;background:linear-gradient(170deg,#8a6e52 0%,#d8cfc4 35%,#b9b2ab 65%,#6b6760 100%)}
.mission-label{left:661px;top:1295px}
.mission-label::after{width:246px}
.mission-title{left:658px;top:1322px;width:420px;font-size:27px;line-height:30px}
.mission-btn{left:657px;top:1465px;width:130px;height:32px}

/* monitors */
.monitors{left:0;top:1721px;width:1200px;height:583px;background:var(--navy)}
.monitors-title{left:0;top:1797px;width:1200px;text-align:center;font-size:27px;color:var(--white)}
.monitors-ring{left:410px;top:1843px;width:380px;height:380px;border:2px solid rgba(255,255,255,.06);border-radius:50%}
.monitors-core{left:512px;top:1945px;width:176px;height:176px;border:4px solid #2d566c;border-radius:50%}
.hazard{width:68px;height:68px;border-radius:50%;background:#2a5165;display:flex;align-items:center;justify-content:center}
.hazard svg{width:36px;height:36px}
.hazard-label{font-size:13.5px;font-weight:700;color:var(--white);white-space:nowrap}

/* stories */
.stories{left:0;top:2304px;width:1200px;height:611px;background:var(--paper)}
.stories-label{left:99px;top:2382px}
.stories-label::after{width:78px}
.stories-title{left:97px;top:2408px;font-size:27px}
.quote-mark{left:411px;top:2388px;width:62px;height:46px}
.stories-text{left:96px;top:2477px;width:430px;font-size:11.5px;line-height:16px;color:var(--text)}
.stories-author{left:96px;top:2572px;font-size:12.5px;line-height:17px;font-weight:700;color:#111}
.dots{left:95px;top:2653px;display:flex;gap:8px;align-items:center}
.dots span{width:5px;height:5px;border-radius:50%;background:var(--ink)}
.dots .on{width:14px;height:14px;border:1.5px solid var(--ink);background:radial-gradient(circle,var(--ink) 3px,transparent 3.5px)}
.photo-frame-2{left:599px;top:2411px;width:60px;height:397px;background:#e4e9eb}
.photo-portrait{left:631px;top:2381px;width:474px;height:457px;background:linear-gradient(120deg,#4d4f53 0%,#9fa6ab 40%,#c9ccd0 60%,#5b4636 100%)}

/* cta */
.cta{left:0;top:2915px;width:1200px;height:247px;background:var(--navy);overflow:hidden}
.cta-ring{left:95px;top:2876px;width:320px;height:320px;border:9px solid #264c61;border-radius:50%}
.cta-title{left:506px;top:2971px;font-size:35px;color:var(--white)}
.cta-text{left:506px;top:3023px;width:470px;font-size:12.5px;line-height:18px;font-weight:600;color:var(--white)}
.cta-btn{left:504px;top:3077px;width:131px;height:31px;border-color:var(--white);color:var(--white)}

/* footer */
.foot-brand{left:204px;top:3223px;display:flex;align-items:center;gap:18px}
.foot-brand .brand-dot{width:50px;height:50px}
.foot-brand .brand-name{color:var(--ink);font-size:36px;font-weight:400;letter-spacing:6px}
.socials{left:249px;top:3320px;display:flex;gap:14px}
.socials span{width:11px;height:11px;border-radius:50%;background:#8a959c}
.foot-col{top:3246px}
.foot-col h4{font-size:10px;font-weight:700;color:var(--ink);padding-bottom:8px;border-bottom:1px solid #ccd3d7;width:96px;margin-bottom:20px}
.foot-col ul{list-style:none;font-size:10.5px;line-height:15.6px;color:#6e7a83}
.foot-col li{display:flex;gap:5px;align-items:flex-start}
.foot-col li svg{width:9px;height:10px;margin-top:2px;flex:none}
.copyright{left:0;top:3420px;width:1200px;text-align:center;font-size:8.5px;font-weight:600;color:#55636c}
</style>
</head>
<body>

<div class="abs hero" role="img" aria-label="Night view of Earth from orbit with glowing city lights"></div>
<svg class="abs hero-arcs" viewBox="0 0 1200 800" aria-hidden="true">
  <path d="M0 624 Q600 340 1200 624 L1200 800 L0 800 Z" fill="#ffffff"/>
  <path d="M-20 665 Q600 361 1220 665" fill="none" stroke="#f0b323" stroke-width="1.6"/>
  <path d="M-20 710 Q600 402 1220 710" fill="none" stroke="#f0b323" stroke-width="1.6"/>
  <path d="M-20 767 Q600 435 1220 767" fill="none" stroke="#f0b323" stroke-width="1.6"/>
</svg>

<div class="abs brand"><span class="brand-dot"></span><span class="brand-name">VOLT</span></div>
<nav class="abs nav"><span class="active">HOME</span><span>FEATURES</span><span>PRICING</span><span>REGISTER</span><span>LOGIN</span></nav>
<h1 class="abs display hero-title">Monitoring natural hazards from<br>space web application</h1>
<div class="abs btn-outline hero-btn">Learn more</div>

<!-- features -->
<div class="abs mark-ring"></div>
<div class="abs eyebrow features-label">Product features</div>
<h2 class="abs display features-title">Dedicated to the monitoring of natural hazards in humanitarian camps around the world.</h2>

<div class="abs card" style="left:581px;top:740px">
  <div class="card-head">
    <svg viewBox="0 0 52 52" fill="none" stroke="#0b2e44" stroke-width="1.6"><path d="M6 26 L26 8 L46 26"/><path d="M12 22 V38 H40 V22"/><rect x="22" y="28" width="8" height="10"/><path d="M4 44 q5 -4 10 0 t10 0 t10 0 t10 0"/></svg>
    <span class="card-title">Consectetur</span>
  </div>
  <p class="card-text">Lorem ipsum dolor sit amet, con sectetur adipiscing elit, sed do eiusmod tempor incididunt.</p>
</div>
<div class="abs card" style="left:852px;top:740px">
  <div class="card-head">
    <svg viewBox="0 0 52 52" fill="none" stroke="#0b2e44" stroke-width="1.6"><path d="M4 44 L10 20 L20 26 L32 20 L44 26 L48 44 Z"/><path d="M32 30 C24 20 24 8 32 8 C40 8 40 20 32 30 Z"/><circle cx="32" cy="15" r="3"/></svg>
    <span class="card-title">Incididunt ut</span>
  </div>
  <p class="card-text">Lorem ipsum dolor sit amet, con sectetur adipiscing elit, sed do eiusmod tempor incididunt.</p>
</div>
<div class="abs card" style="left:581px;top:935px">
  <div class="card-head">
    <svg viewBox="0 0 52 52" fill="none" stroke="#0b2e44" stroke-width="1.6"><path d="M4 40 L18 14 L30 34 L36 26 L46 40"/><circle cx="40" cy="38" r="2.5"/><circle cx="46" cy="34" r="2"/></svg>
    <span class="card-title">Adipiscing</span>
  </div>
  <p class="card-text">Lorem ipsum dolor sit amet, con sectetur adipiscing elit, sed do eiusmod tempor incididunt.</p>
</div>
<div class="abs card" style="left:852px;top:935px">
  <div class="card-head">
    <svg viewBox="0 0 52 52" fill="none" stroke="#0b2e44" stroke-width="1.6"><rect x="4" y="4" width="44" height="44" rx="2"/><path d="M10 38 L20 24 L28 32 L40 14"/><path d="M14 46 V36 M24 46 V32 M34 46 V30"/></svg>
    <span class="card-title">Exercitation</span>
  </div>
  <p class="card-text">Lorem ipsum dolor sit amet, con sectetur adipiscing elit, sed do eiusmod tempor incididunt.</p>
</div>

<!-- mission -->
<section class="abs mission"></section>
<div class="abs photo-night" role="img" aria-label="Satellite view of a city at night along a river"></div>
<div class="abs photo-frame"></div>
<div class="abs photo-couple" role="img" aria-label="Two people working on laptops on a sofa"></div>
<div class="abs eyebrow mission-label">Our mission</div>
<h2 class="abs display mission-title">To hide to the users' all the complexity of the satellite image processing and just provide them the results.</h2>
<div class="abs btn-outline mission-btn">More about us</div>

<!-- monitors -->
<section class="abs monitors"></section>
<h2 class="abs display monitors-title">What VOLT monitors</h2>
<div class="abs monitors-ring"></div>
<div class="abs monitors-core"></div>

<div class="abs hazard" style="left:404px;top:1886px"><svg viewBox="0 0 36 36" fill="none" stroke="#fff" stroke-width="1.4"><path d="M10 18 a6 6 0 0 1 2-11 a8 8 0 0 1 14 2 a5 5 0 0 1 0 9 Z"/><path d="M13 22 l-2 5 M19 22 l-2 5 M25 22 l-2 5"/><path d="M5 31 q4 -3 8 0 t8 0 t8 0"/></svg></div>
<div class="abs hazard-label" style="right:811px;top:1911px">Lorem ipsum dolor sit amet</div>
<div class="abs hazard" style="left:373px;top:1999px"><svg viewBox="0 0 36 36" fill="none" stroke="#fff" stroke-width="1.4"><path d="M5 8 H31 M8 13 H28 M11 18 H25 M13 23 H22 M15 28 H20"/></svg></div>
<div class="abs hazard-label" style="right:842px;top:2025px">Lorem ipsum dolor sit amet</div>
<div class="abs hazard" style="left:404px;top:2113px"><svg viewBox="0 0 36 36" fill="none" stroke="#fff" stroke-width="1.4"><path d="M9 24 a6 6 0 0 1 1-12 a8 8 0 0 1 15 1 a5.5 5.5 0 0 1 1 11 Z"/><path d="M18 16 l-3 6 h4 l-3 6"/></svg></div>
<div class="abs hazard-label" style="right:811px;top:2138px">Lorem ipsum dolor sit amet</div>

<div class="abs hazard" style="left:726px;top:1886px"><svg viewBox="0 0 36 36" fill="none" stroke="#fff" stroke-width="1.4"><path d="M18 4 C24 12 28 16 28 23 a10 10 0 0 1 -20 0 C8 17 12 14 14 9 C15 14 17 15 18 4 Z"/><path d="M18 31 a4 4 0 0 1 -4 -5 c1 -3 4 -4 4 -8 c2 3 4 5 4 8 a4 4 0 0 1 -4 5"/></svg></div>
<div class="abs hazard-label" style="left:810px;top:1911px">Lorem ipsum dolor sit amet</div>
<div class="abs hazard" style="left:757px;top:1999px"><svg viewBox="0 0 36 36" fill="none" stroke="#fff" stroke-width="1.4"><path d="M3 30 L14 10 L22 24 L26 18 L33 30 Z"/><circle cx="28" cy="26" r="2"/><circle cx="32" cy="22" r="1.5"/></svg></div>
<div class="abs hazard-label" style="left:841px;top:2025px">Lorem ipsum dolor sit amet</div>
<div class="abs hazard" style="left:726px;top:2113px"><svg viewBox="0 0 36 36" fill="none" stroke="#fff" stroke-width="1.4"><path d="M14 16 L22 8 L30 16 V26 H14 Z"/><rect x="20" y="19" width="4" height="7"/><path d="M6 18 l4 8 l-3 0 l3 7"/></svg></div>
<div class="abs hazard-label" style="left:810px;top:2138px">Lorem ipsum dolor sit amet</div>

<!-- stories -->
<section class="abs stories"></section>
<div class="abs eyebrow stories-label">Success stories</div>
<h2 class="abs display stories-title">What they say about VOLT</h2>
<svg class="abs quote-mark" viewBox="0 0 62 46" aria-hidden="true"><path d="M0 46 V24 C0 10 8 2 24 0 V10 C16 12 13 16 13 22 H26 V46 Z M35 46 V24 C35 10 43 2 59 0 V10 C51 12 48 16 48 22 H62 V46 Z" fill="#0b2e44"/></svg>
<p class="abs stories-text">Lorem ipsum dolor sit amet, consectetur adipiscing elit, sed do eius mod tempor incididunt ut labore et dolore magna aliqua. Ut enim ad minim veniam, quis nostrud exercitation ullamco laboris nisi ut aliqu ip ex ea commodo consequat.</p>
<p class="abs stories-author">Daniel Harlow<br>VP, Digital Transformation and IT,<br>Norvane</p>
<div class="abs dots"><span class="on"></span><span></span><span></span></div>
<div class="abs photo-frame-2"></div>
<div class="abs photo-portrait" role="img" aria-label="Portrait of a smiling man in a waistcoat seated at a desk"></div>

<!-- cta -->
<section class="abs cta"></section>
<div class="abs cta-ring"></div>
<h2 class="abs display cta-title">Ready to get started</h2>
<p class="abs cta-text">Lorem ipsum dolor sit amet, consectetur adipiscing elit, sed do eiusmod tempor incididunt ut labore et dolore magna aliqua.</p>
<div class="abs btn-outline cta-btn">Register now!</div>

<!-- footer -->
<div class="abs foot-brand"><span class="brand-dot"></span><span class="brand-name">VOLT</span></div>
<div class="abs socials" aria-label="Social links"><span></span><span></span><span></span><span></span><span></span></div>

<div class="abs foot-col" style="left:487px"><h4>QUICK LINKS</h4>
  <ul><li>Home</li><li>Features</li><li>Pricing</li><li>Register</li><li>Login</li></ul></div>
<div class="abs foot-col" style="left:647px"><h4>PRICING</h4>
  <ul><li>Silver Package</li><li>Gold Package</li><li>Platinum Package</li></ul></div>
<div class="abs foot-col" style="left:836px"><h4 style="width:160px">CONTACT</h4>
  <ul>
    <li><svg viewBox="0 0 9 10"><path d="M4.5 10 C1.5 6 1 5 1 3.5 a3.5 3.5 0 0 1 7 0 C8 5 7.5 6 4.5 10 Z" fill="#0b2e44"/><circle cx="4.5" cy="3.5" r="1.2" fill="#fff"/></svg><span>12 Rue des Tilleuls,<br>L-4410 Belvaux,<br>Luxembourg</span></li>
    <li style="margin-top:15px"><svg viewBox="0 0 9 10"><rect x="0" y="2" width="9" height="6" fill="#0b2e44"/><path d="M0 2 L4.5 5.5 L9 2" stroke="#fff" fill="none" stroke-width=".8"/></svg><span>info@kormel.cloud</span></li>
  </ul></div>

<p class="abs copyright">© COPYRIGHT 2024 KORMEL SARL I &nbsp;ALL RIGHTS RESERVED</p>

</body>
</html>
```